A new PowerPoint Template for a French consulting company

Who are we?

Formed in 2005, Orvanel is a consulting company specialising in the human aspect of change and transformation.

From our offices in the heart of Paris, our team of 30 consultants work with leading organisations in the Aerospace, Finance, Transportation and Public sectors to deliver lasting change.

Our customers trust us with some of their most strategic and sensitive projects. They trust us with these projects because:
- We listen to them, ensuring we understand the real needs of their business
- We involve them, co-developing and tailoring our solutions to the specific challenges they face
- We’re professional, without taking ourselves too seriously
- We’re imaginative, whilst always remaining pragmatic
- We get results!

You can find out more about who we are and the work we do here: http://www.orvanel-conseil.fr/en

What we need from you?

We’re approaching our 10th birthday and, whilst we still love what we do, we think it’s the right time to update our image.

We’d like you to design us a new PowerPoint template, that will be used for all of our internal and client facing work. You can base your submissions on our existing logo and colour scheme (see files attached) or you can submit your own fresh ideas – after all, we’re not afraid of change!

Finally, whilst we’re looking for you to be creative, there are some simple guidelines that we need you to keep in mind:

1. The Template needs to include both a front cover and a “content” page

2. The front cover needs to:
- Include our logo
- Reflect “who we are” and the type of work that we do

3. The content page needs to:
- Have a predominantly white background
- Be practical to use, making an effective use of the 4:3 standard PPT size
- Include an area across the top of the page for the slide title
- Include areas along the bottom of the page for the page number and date

4. If you decide to propose a new colour scheme, it should be balanced and the “accents” usable

5. The PowerPoint Template needs to be “printer friendly”

6. The fonts you use should be standard

What we don’t want?

To give you as much help as possible, here are some things that we really don’t want:

- Submissions that are dull grey or navy blue, suggesting we’re nothing but boring corporate suits
- Submissions that are Barbie pink or too “soft and cuddly”
- Submissions that use lots of stock images of “happy, smiling, consultants”
- Submissions that will be the height of fashion today, but completely out of date next year

Industry/Entity Type

It Company

```html
<!DOCTYPE html>
<html lang="en">
<head>
<meta charset="utf-8">
<title>Orvanel — Presentation Template</title>
<link rel="stylesheet" href="https://fonts.googleapis.com/css2?family=Open+Sans:ital,wght@0,400;0,600;0,700;1,400&display=swap">
<style>
  :root {
    --board: #a9b1b6;
    --plum: #8c1150;
    --plum-deep: #6d0a3e;
    --teal: #00aaa5;
    --ink: #4a4a4a;
    --band: #f4f4f5;
    --placeholder: #e7e7e8;
    --white: #ffffff;
  }
  * { margin: 0; padding: 0; box-sizing: border-box; }
  html, body { width: 1200px; height: 905px; overflow: hidden; }
  body {
    background: var(--board);
    font-family: "Open Sans", Arial, sans-serif;
    position: relative;
  }
  .slide {
    position: absolute;
    width: 582px;
    height: 434px;
    background: var(--white);
    overflow: hidden;
  }
  .slide--cover { left: 14px; top: 12px; background: radial-gradient(ellipse at 50% 45%, #f7f7f8 0%, #e9e9eb 70%, #dedee1 100%); }
  .slide--title { left: 606px; top: 12px; }
  .slide--image { left: 14px; top: 458px; }
  .slide--graph { left: 606px; top: 458px; }

  .brand-name {
    position: absolute;
    left: 0;
    width: 582px;
    text-align: center;
    color: var(--plum);
    font-weight: 600;
    line-height: 1;
    letter-spacing: -0.02em;
    white-space: nowrap;
  }
  .slide--cover .brand-name { top: 160px; font-size: 104px; }
  .slide--title .brand-name { top: 128px; font-size: 58px; color: var(--plum-deep); }

  .deck-title { position: absolute; right: 26px; top: 283px; font-size: 18px; color: #555; font-weight: 400; letter-spacing: 0.01em; }
  .deck-date { position: absolute; right: 26px; top: 306px; font-size: 11px; color: var(--plum); font-weight: 600; }
  .cover-band {
    position: absolute; left: 0; top: 348px; width: 582px; height: 86px;
    background: linear-gradient(90deg, var(--band) 60%, #ececee 100%);
    border-bottom: 3px solid var(--teal);
  }
  .cover-band__title { position: absolute; left: 25px; top: 26px; font-size: 16px; color: var(--plum-deep); }
  .cover-band__title strong { font-weight: 700; }
  .cover-band__sub { position: absolute; left: 27px; top: 47px; font-size: 10px; color: var(--teal); }
  .cover-band__sub strong { font-weight: 700; }
  .client-slot {
    position: absolute; left: 501px; top: 18px; width: 67px; height: 52px;
    border: 1.5px solid var(--plum-deep); background: var(--white);
    display: flex; align-items: center; justify-content: center;
  }

  .slide-header {
    position: absolute; left: 0; top: 0; width: 582px; height: 40px;
    background: linear-gradient(90deg, var(--band) 70%, #ececee 100%);
    border-top: 2px solid var(--teal);
  }
  .slide-header__title { position: absolute; left: 15px; top: 9px; font-size: 18px; color: var(--plum-deep); letter-spacing: 0.01em; white-space: nowrap; }
  .slide-header__sub { font-size: 8.5px; color: var(--teal); margin-left: 8px; vertical-align: 3px; }
  .slide-header__sub strong { font-weight: 700; }

  .image-slot {
    position: absolute; left: 38px; top: 72px; width: 505px; height: 224px;
    background: var(--placeholder); border: 1px solid #e3cfd8;
    display: flex; align-items: center; justify-content: center;
  }
  .bullets { position: absolute; left: 40px; top: 313px; width: 501px; list-style: none; }
  .bullets li {
    position: relative; padding-left: 16px; margin-bottom: 12px;
    font-size: 7.5px; line-height: 1.5; color: var(--ink); text-align: justify;
  }
  .bullets li::before {
    content: ""; position: absolute; left: 0; top: 3px;
    border-left: 4px solid var(--teal); border-top: 3px solid transparent; border-bottom: 3px solid transparent;
  }
  .bullets strong { font-weight: 700; }

  .slide-footer {
    position: absolute; left: 0; bottom: 0; width: 582px; height: 36px; background: var(--band);
    display: flex; align-items: center; padding: 0 18px 0 15px;
  }
  .slide-footer__brand { font-size: 17px; color: var(--plum-deep); font-weight: 600; letter-spacing: -0.02em; line-height: 1; }
  .slide-footer__label { margin-left: 8px; font-size: 8px; color: var(--teal); }
  .slide-footer__label strong { font-weight: 700; }
  .slide-footer__page { margin-left: auto; font-size: 8px; color: var(--teal); font-weight: 700; }

  .graph { position: absolute; left: 0; top: 40px; }
  .graph text { font-family: "Open Sans", Arial, sans-serif; }
</style>
</head>
<body>

<section class="slide slide--cover">
  <div class="brand-name">Orvanel</div>
</section>

<section class="slide slide--title">
  <div class="brand-name">Orvanel</div>
  <div class="deck-title">PRESENTATION TITLE</div>
  <div class="deck-date">JAN 2014</div>
  <div class="cover-band">
    <div class="cover-band__title"><strong>COMPANY</strong> PRESENTATION</div>
    <div class="cover-band__sub">to <strong>Business</strong>/Client</div>
    <div class="client-slot">
      <svg width="26" height="24" viewBox="0 0 26 24" aria-hidden="true">
        <rect x="1" y="1" width="24" height="22" fill="none" stroke="#6d0a3e" stroke-width="2"/>
        <circle cx="8" cy="8" r="2.5" fill="#6d0a3e"/>
        <path d="M4 20 L11 12 L15 16 L18 13 L22 20 Z" fill="#6d0a3e"/>
      </svg>
    </div>
  </div>
</section>

<section class="slide slide--image">
  <header class="slide-header">
    <div class="slide-header__title">IMAGE IN LANDSCAPE VIEW<span class="slide-header__sub">WITH COMPLETELY <strong>CUSTOMIZABLE</strong> ICONS</span></div>
  </header>
  <div class="image-slot" role="img" aria-label="Landscape image placeholder">
    <svg width="108" height="108" viewBox="0 0 108 108" aria-hidden="true">
      <rect x="4" y="4" width="100" height="100" fill="none" stroke="#f3f3f4" stroke-width="7"/>
      <circle cx="30" cy="30" r="10" fill="#f3f3f4"/>
      <path d="M14 90 L42 56 L56 72 L74 46 L96 90 Z" fill="#f3f3f4"/>
    </svg>
  </div>
  <ul class="bullets">
    <li><strong>Aenean</strong> ridiculus tortor quis interdum id habitant ad, natoque consectetuer nisl auctor libero quisque euismod ante inceptos malesuada ligula mattis.</li>
    <li><strong>Aenean</strong> ridiculus tortor quis interdum id habitant ad, natoque consectetuer nisl auctor libero quisque euismod ante inceptos malesuada ligula mattis.</li>
  </ul>
  <footer class="slide-footer">
    <span class="slide-footer__brand">Orvanel</span>
    <span class="slide-footer__label">| <strong>COMPANY</strong> PRESENTATION</span>
    <span class="slide-footer__page">3</span>
  </footer>
</section>

<section class="slide slide--graph">
  <header class="slide-header">
    <div class="slide-header__title">STYLE GRAPHS</div>
  </header>
  <svg class="graph" width="582" height="358" viewBox="0 40 582 358">
    <circle cx="291" cy="217" r="135" fill="none" stroke="#a8dcd9" stroke-width="1" stroke-dasharray="2 3"/>
    <g stroke="#00aaa5" stroke-width="2">
      <line x1="291" y1="217" x2="291" y2="84"/>
      <line x1="291" y1="217" x2="388" y2="128"/>
      <line x1="291" y1="217" x2="424" y2="217"/>
      <line x1="291" y1="217" x2="394" y2="302"/>
      <line x1="291" y1="217" x2="291" y2="346"/>
      <line x1="291" y1="217" x2="193" y2="302"/>
      <line x1="291" y1="217" x2="160" y2="217"/>
      <line x1="291" y1="217" x2="193" y2="125"/>
    </g>
    <circle cx="291" cy="217" r="79" fill="#00aaa5"/>
    <rect x="251" y="164" width="80" height="78" rx="14" fill="#4cc5c1" role="img" aria-label="Team icon"/>
    <text x="291" y="260" text-anchor="middle" font-size="10" font-style="italic" fill="#ffffff">change</text>
    <text x="291" y="273" text-anchor="middle" font-size="10" font-style="italic" fill="#ffffff">management</text>

    <g stroke-width="2" fill="#ffffff">
      <circle cx="291" cy="84" r="30" stroke="#c81d6f"/>
      <circle cx="388" cy="128" r="30" stroke="#0d9e8a"/>
      <circle cx="424" cy="217" r="30" stroke="#5b7fe0"/>
      <circle cx="394" cy="302" r="30" stroke="#a8c400"/>
      <circle cx="291" cy="346" r="30" stroke="#6d0a3e"/>
      <circle cx="193" cy="302" r="30" stroke="#f3a200"/>
      <circle cx="160" cy="217" r="30" stroke="#d2609a"/>
      <circle cx="193" cy="125" r="30" stroke="#4fd1c5"/>
    </g>
    <g>
      <rect x="282" y="70" width="18" height="28" rx="5" fill="#c81d6f" role="img" aria-label="Person icon"/>
      <rect x="379" y="114" width="18" height="28" rx="5" fill="#0d9e8a" role="img" aria-label="Person icon"/>
      <rect x="415" y="203" width="18" height="28" rx="5" fill="#5b7fe0" role="img" aria-label="Person icon"/>
      <rect x="385" y="288" width="18" height="28" rx="5" fill="#a8c400" role="img" aria-label="Person icon"/>
      <rect x="282" y="332" width="18" height="28" rx="5" fill="#6d0a3e" role="img" aria-label="Person icon"/>
      <rect x="184" y="288" width="18" height="28" rx="5" fill="#f3a200" role="img" aria-label="Person icon"/>
      <rect x="151" y="203" width="18" height="28" rx="5" fill="#d2609a" role="img" aria-label="Person icon"/>
      <rect x="184" y="111" width="18" height="28" rx="5" fill="#4fd1c5" role="img" aria-label="Person icon"/>
    </g>
    <g font-size="8" font-weight="600">
      <text x="232" y="65" fill="#c81d6f">TITLE</text>
      <text x="432" y="131" fill="#0d9e8a">TITLE</text>
      <text x="461" y="225" fill="#5b7fe0">TITTLER</text>
      <text x="437" y="310" fill="#a8c400">TITLE</text>
      <text x="327" y="379" fill="#6d0a3e">TITLE</text>
      <text x="131" y="319" fill="#f3a200">TITLE</text>
      <text x="93" y="220" fill="#d2609a">TITLE</text>
      <text x="131" y="124" fill="#7fb2d9">TITLE</text>
    </g>
  </svg>
  <footer class="slide-footer">
    <span class="slide-footer__brand">Orvanel</span>
    <span class="slide-footer__label">| <strong>COMPANY</strong> PRESENTATION</span>
    <span class="slide-footer__page">6</span>
  </footer>
</section>

</body>
</html>
```